Rack Card for Portuguese Walking Food Tour

I would like a vertical rack card measuring 99x210mm. Here is the information I would like to include. It does not need to be in this format. We are located in Setubal, Portugal.
Please use the attached Teal Heron Logo.
Setúbal: Tradition and Today
Experience the culinary delights of Setúbal, Portugal with a walking food tour around our waterfront village. Discover the Mercado da Gaivota Branca, voted one of the world’s best markets by Metro Ledger, and indulge in local wines and dishes. Prepare for a calm stroll on flat streets. No hills to climb on this tour.
Duration: 4 hours
www.brinebasketwalks.com
+351 265 000 487

```html
<!DOCTYPE html>
<html lang="en">
<head>
<meta charset="utf-8">
<title>Brine Basket Walks – Setúbal Rack Card</title>
<link rel="stylesheet" href="https://fonts.googleapis.com/css2?family=Montserrat:wght@700;800&family=Pacifico&family=Raleway:wght@400&family=Yellowtail&display=swap">
<style>
  :root {
    --orange: #f26522;
    --peach: #fdebe4;
    --white: #ffffff;
    --photo-wine: #6f7688;
    --photo-fish: #d88266;
    --photo-oyster: #d6d4cf;
    --photo-charcuterie: #c79463;
    --photo-market: #b39a78;
  }
  html, body { margin: 0; padding: 0; }
  body { width: 1200px; height: 2545px; overflow: hidden; background: var(--white); }
  .rack-card { position: relative; width: 1200px; height: 2545px; overflow: hidden; background: var(--white); font-family: "Raleway", sans-serif; }

  .backdrop-ring {
    position: absolute; left: -60px; top: 150px; width: 1110px; height: 1330px;
    border-radius: 50%; border: 200px solid var(--peach); box-sizing: border-box;
  }
  .backdrop-lower {
    position: absolute; left: 300px; top: 1900px; width: 900px; height: 700px;
    background: var(--peach); clip-path: polygon(30% 0, 100% 0, 100% 100%, 0 100%, 0 40%);
  }

  .frame {
    position: absolute; left: 56px; top: 53px; width: 1088px; height: 2700px;
    border: 6px solid var(--orange); border-radius: 72px; box-sizing: border-box;
  }

  .brand { position: absolute; left: 190px; top: 150px; display: flex; align-items: center; gap: 40px; }
  .brand-dot { width: 180px; height: 180px; border-radius: 50%; background: var(--orange); }
  .brand-name {
    font-family: "Montserrat", sans-serif; font-weight: 800; color: var(--orange);
    font-size: 74px; line-height: 1.05; letter-spacing: 1px;
  }

  .headline { position: absolute; left: 0; width: 1200px; top: 540px; text-align: center; color: var(--orange); }
  .headline-place { font-family: "Yellowtail", "Pacifico", cursive; font-size: 170px; line-height: 1; height: 160px; }
  .headline-sub { font-family: "Montserrat", sans-serif; font-weight: 800; font-size: 82px; letter-spacing: -1px; margin-top: -6px; padding-left: 20px; }
  .divider { position: absolute; left: 493px; top: 822px; width: 226px; height: 21px; border-radius: 11px; background: var(--orange); }

  .intro {
    position: absolute; left: 146px; top: 875px; width: 908px; margin: 0;
    color: var(--orange); font-size: 45.5px; line-height: 76px; text-align: justify;
  }

  .details {
    position: absolute; left: -10px; top: 1531px; width: 892px; height: 274px;
    border: 6px solid var(--orange); border-left: none; border-radius: 0 137px 137px 0; box-sizing: border-box;
    font-family: "Montserrat", sans-serif; font-weight: 700; color: var(--orange);
  }
  .details-duration { position: absolute; left: 156px; top: 22px; font-size: 46px; line-height: 56px; white-space: nowrap; }
  .details-web { position: absolute; left: 156px; top: 78px; font-size: 46px; line-height: 56px; letter-spacing: -0.5px; white-space: nowrap; }
  .details-phone { position: absolute; left: 70px; top: 150px; display: flex; align-items: center; gap: 30px; font-size: 68px; white-space: nowrap; }
  .details-phone svg { width: 62px; height: 62px; }

  .photo {
    position: absolute; border: 10px solid var(--orange); border-radius: 22%;
    transform: rotate(45deg); box-sizing: border-box;
  }
  .photo-wine { left: -300px; top: 1880px; width: 820px; height: 820px; background: var(--photo-wine); border-width: 14px; }
  .photo-fish { left: 573px; top: 2022px; width: 208px; height: 208px; background: var(--photo-fish); }
  .photo-oyster { left: 855px; top: 1715px; width: 470px; height: 470px; background: var(--photo-oyster); border-width: 12px; }
  .photo-charcuterie { left: 890px; top: 2225px; width: 520px; height: 520px; background: var(--photo-charcuterie); border-width: 12px; }
  .photo-market { left: 440px; top: 2425px; width: 475px; height: 475px; background: var(--photo-market); border-width: 12px; }
</style>
</head>
<body>
<main class="rack-card">
  <div class="backdrop-ring"></div>
  <div class="backdrop-lower"></div>
  <div class="frame"></div>

  <header class="brand">
    <div class="brand-dot"></div>
    <div class="brand-name">Brine Basket<br>Walks</div>
  </header>

  <section class="headline">
    <div class="headline-place">Setúbal</div>
    <div class="headline-sub">TRADITION &amp; TODAY</div>
  </section>
  <div class="divider"></div>

  <p class="intro">Experience the culinary delights of Setúbal, Portugal with a walking food tour around our waterfront village. Discover the Mercado da Gaivota Branca, voted one of the world's best markets by Metro Ledger, and indulge in local wines and dishes. Prepare for a calm stroll on flat streets. No hills to climb on this tour.</p>

  <section class="details">
    <div class="details-duration">Duration: 4 hours</div>
    <div class="details-web">www.brinebasketwalks.com</div>
    <div class="details-phone">
      <svg viewBox="0 0 24 24" fill="none" stroke="var(--orange)" stroke-width="2.4" stroke-linecap="round" stroke-linejoin="round" aria-hidden="true">
        <path d="M22 16.9v3a2 2 0 0 1-2.2 2 19.8 19.8 0 0 1-8.6-3.1 19.5 19.5 0 0 1-6-6A19.8 19.8 0 0 1 2.1 4.2 2 2 0 0 1 4.1 2h3a2 2 0 0 1 2 1.7c.1 1 .4 1.9.7 2.8a2 2 0 0 1-.5 2.1L8 9.9a16 16 0 0 0 6 6l1.3-1.3a2 2 0 0 1 2.1-.4c.9.3 1.8.6 2.8.7a2 2 0 0 1 1.7 2z"/>
        <path d="M15 5a5 5 0 0 1 4 4M15 1a9 9 0 0 1 8 8"/>
      </svg>
      <span>+351 265 000 487</span>
    </div>
  </section>

  <div class="photo photo-wine" role="img" aria-label="Photo of a glass of beer and a glass of white wine on a café table with cured ham"></div>
  <div class="photo photo-fish" role="img" aria-label="Photo of fresh red mullet at the fish market"></div>
  <div class="photo photo-oyster" role="img" aria-label="Photo of fresh oysters on ice with lemon wedges"></div>
  <div class="photo photo-charcuterie" role="img" aria-label="Photo of sliced chouriço sausage with toasted bread"></div>
  <div class="photo photo-market" role="img" aria-label="Photo of sacks of dried beans with price tags at the market"></div>
</main>
</body>
</html>
```